Existing graphics (3D cube) should be made more understandable

Hi,
I would like to make my 3D cube more understandable, but it should also be more presentable. I have attached a detailed description as an attachment. I think the image so far is good, but if we can improve it (more understandable and prettier), I would be happy.
BR
Rob

Target Market(s)

Students, Teachers, Prof.

Colors
0054AA
0677BA
7BADD7
CADEEF
E8F1F8
0094D4
00A9DD
6FCCEA
C7EBF8
E9F6FB
00AB8E
00BBA5
67D7C9
C6EFE9
E9F9F6
59FF00
82FF00
B8FF75
E3FFCB
F4FFEA

Requirements
Must have
• please see attachment
Nice to have
• please see attachment
Should not have
• please see attachment

```html
<!DOCTYPE html>
<html lang="en">
<head>
<meta charset="utf-8">
<title>Ambidextrous Leadership Cube</title>
<link rel="stylesheet" href="https://fonts.googleapis.com/css2?family=Inter:wght@400;600;700&display=swap">
<style>
:root{
  --bg-top:#f7f7f8;
  --bg-bottom:#ececee;
  --ink:#2b2b2b;
  --axis:#3a3a3a;
  --note-bg:#e6e6e8;
  --area-1:#0cb9a4;
  --area-1-top:#84d0c4;
  --area-2:#8dc63f;
  --area-2-top:#a9d15f;
  --area-2-side:#c3df90;
  --area-3-top:#0f57a8;
  --area-3-side:#7ca3d4;
  --area-4:#05673a;
  --area-4-side:#69a678;
  --area-5:#1a93d3;
  --tag-1:#00ab8e;
  --tag-2:#8dc63f;
  --tag-3:#0f57a8;
  --tag-4:#05673a;
  --tag-5:#1a93d3;
}
*{box-sizing:border-box;margin:0;padding:0}
html,body{width:927px;height:1200px;overflow:hidden}
body{
  font-family:"Inter",Arial,sans-serif;
  background:radial-gradient(ellipse at 50% 35%,var(--bg-top) 0%,var(--bg-bottom) 100%);
  position:relative;color:var(--ink);
}
.diagram{position:absolute;left:0;top:0}
.note{position:absolute;background:var(--note-bg);font-size:12px;line-height:15px;color:#333;padding:8px 9px}
.note--y{left:186px;top:346px;width:160px;height:50px}
.note--x{left:564px;top:814px;width:153px;height:42px}
.note--high{left:549px;top:264px;width:207px;height:119px;padding:10px 12px}
.note--high .note-title{font-weight:600;font-size:15px;padding-bottom:8px;border-bottom:1px solid #888;margin-bottom:9px}
.legend{position:absolute;font-size:13px;line-height:16px;color:#333}
.tag{display:inline-block;color:#fff;font-weight:700;font-size:13px;padding:1px 7px;margin-bottom:5px}
.legend--1{left:155px;top:584px}
.legend--1 .tag{margin-left:17px;background:var(--tag-1)}
.legend--5{left:144px;top:719px}
.legend--5 .tag{margin-left:30px;background:var(--tag-5)}
.legend--3{left:663px;top:442px}
.legend--3 .tag{background:var(--tag-3)}
.legend--2{left:664px;top:548px}
.legend--2 .tag{background:var(--tag-2)}
.legend--4{left:665px;top:658px}
.legend--4 .tag{background:var(--tag-4)}
.scale{position:absolute;font-size:13px;font-weight:600;color:#222}
</style>
</head>
<body>
<svg class="diagram" width="927" height="1200" viewBox="0 0 927 1200">
  <!-- top faces -->
  <polygon points="260,545 385,420 510,420 450,483 385,545" fill="var(--area-1-top)"/>
  <polygon points="450,483 510,420 635,420 575,483" fill="var(--area-3-top)"/>
  <polygon points="385,545 450,483 575,483 510,545" fill="var(--area-2-top)"/>
  <!-- right faces -->
  <polygon points="575,483 635,420 635,545 575,608" fill="var(--area-3-side)"/>
  <polygon points="510,545 575,483 575,608 510,670" fill="var(--area-2-side)"/>
  <polygon points="510,670 575,608 635,545 635,670 510,795" fill="var(--area-4-side)"/>
  <!-- front faces -->
  <rect x="260" y="545" width="125" height="125" fill="var(--area-1)"/>
  <rect x="385" y="545" width="125" height="125" fill="var(--area-2)"/>
  <rect x="260" y="670" width="125" height="125" fill="var(--area-5)"/>
  <rect x="385" y="670" width="125" height="125" fill="var(--area-4)"/>
  <line x1="260" y1="795" x2="510" y2="545" stroke="#1f5a4a" stroke-opacity=".55" stroke-width="1.5"/>
  <!-- roman numerals -->
  <g font-family="Inter,Arial,sans-serif" font-weight="700" font-size="46" fill="#fff" fill-opacity=".8">
    <text x="268" y="596">I</text>
    <text x="397" y="596">II</text>
    <text x="511" y="463">III</text>
    <text x="268" y="724">V</text>
    <text x="397" y="724">IV</text>
  </g>
  <!-- points -->
  <g fill="#fff" font-family="Inter,Arial,sans-serif" font-size="14">
    <circle cx="273" cy="614" r="3"/><text x="269" y="632">L</text>
    <circle cx="499" cy="610" r="3"/><text x="480" y="628">LM</text>
    <circle cx="621" cy="472" r="3"/><text x="614" y="494">A</text>
    <circle cx="369" cy="763" r="3"/><text x="359" y="784">N</text>
    <circle cx="497" cy="763" r="3"/><text x="488" y="784">M</text>
  </g>
  <!-- axes -->
  <g stroke="var(--axis)" stroke-width="2.5" fill="none">
    <line x1="260" y1="796" x2="260" y2="402"/>
    <polyline points="250,412 260,401 270,412"/>
    <line x1="259" y1="795" x2="655" y2="795"/>
    <polyline points="645,785 656,795 645,805"/>
  </g>
  <g stroke="#9fb7d8" stroke-width="3" fill="none">
    <line x1="635" y1="420" x2="657" y2="398"/>
    <polyline points="644,400 658,398 656,412"/>
  </g>
  <g font-family="Inter,Arial,sans-serif" font-size="13" font-weight="600" fill="#222">
    <text transform="translate(222,570) rotate(-45)">Strong</text>
    <text transform="translate(222,692) rotate(-45)">Middle</text>
    <text transform="translate(226,802) rotate(-45)">Weak</text>
  </g>
</svg>

<div class="note note--y">Exploration, leader role, opening leadership</div>
<div class="note note--x">Exploitation, manager role, closing leadership</div>
<div class="note note--high">
  <div class="note-title">High</div>
  Flexible to switch between exploration and exploitation, leader and manager role, opening and closing leadership
</div>

<div class="legend legend--1"><span class="tag">Area I</span><br>Executive for<br>leadership(L)</div>
<div class="legend legend--5"><span class="tag">Area V</span><br>neither nor(N)</div>
<div class="legend legend--3"><span class="tag">Area III</span><br>Executive for<br>ambidextrous<br>leadership(A)</div>
<div class="legend legend--2"><span class="tag">Area II</span><br>Executive for<br>leadership and<br>management</div>
<div class="legend legend--4"><span class="tag">Area IV</span><br>Executive for<br>management(M)</div>

<div class="scale" style="left:258px;top:812px">Weak</div>
<div class="scale" style="left:362px;top:813px">Middle</div>
<div class="scale" style="left:471px;top:812px">Strong</div>
</body>
</html>
```